Biz Card & Stationary: Modern, boutique appeal for vacation rental company for high end luxury homes
Biz Card + Folder + Letterhead + Envelope
Simple
Marla Whitcombe
Owner
2817 Maple Hollow Ln Austin TX 78529
marla@quolbi.com
www.quolbi.com
-may create image or graphic to use with logo -Need letterhead & envelopes in word format

```html
<!DOCTYPE html>
<html lang="en">
<head>
<meta charset="utf-8">
<title>Quolbi Business Card</title>
<link href="https://fonts.googleapis.com/css2?family=Open+Sans:wght@300;400;600&display=swap" rel="stylesheet">
<style>
  :root {
    --backdrop: #2b2b2d;
    --card-white: #ffffff;
    --teal: #35b5c0;
    --teal-deep: #2aa3ae;
    --band-grey: #6e6e70;
    --text-grey: #555558;
  }
  * { margin: 0; padding: 0; box-sizing: border-box; }
  html, body { width: 1200px; height: 646px; overflow: hidden; }
  body {
    background: var(--backdrop);
    font-family: "Open Sans", sans-serif;
    position: relative;
  }
  .card {
    position: absolute;
    top: 173px;
    width: 520px;
    height: 300px;
    border-radius: 16px;
    background: var(--card-white);
    overflow: hidden;
  }
  .card-front { left: 60px; }
  .card-back { left: 620px; }

  .brand {
    position: absolute;
    top: 50%;
    left: 50%;
    transform: translate(-50%, -50%);
    display: flex;
    align-items: center;
    gap: 12px;
  }
  .brand-mark {
    width: 14px; height: 14px;
    border-radius: 50%;
    background: var(--teal);
  }
  .brand-name {
    font-weight: 300;
    font-size: 58px;
    color: var(--teal);
    letter-spacing: 1px;
    line-height: 1;
  }
  .card-back .brand {
    top: 112px; left: 40px;
    transform: none;
  }
  .card-back .brand-name { font-size: 46px; }

  .sweep { position: absolute; inset: 0; }

  .person {
    position: absolute;
    top: 22px; right: 78px;
    text-align: right;
    z-index: 1;
  }
  .person-name {
    font-weight: 600;
    font-size: 16px;
    color: var(--teal);
    line-height: 1.3;
  }
  .person-title {
    font-size: 13px;
    color: var(--text-grey);
    margin-top: 1px;
  }

  .contact {
    position: absolute;
    left: 26px; bottom: 20px;
    color: var(--card-white);
    font-size: 10.5px;
    line-height: 1.45;
  }
  .phones {
    position: absolute;
    right: 26px; bottom: 118px;
    color: var(--card-white);
    font-size: 10.5px;
    line-height: 1.5;
    text-align: right;
  }
</style>
</head>
<body>
  <section class="card card-front">
    <div class="brand">
      <span class="brand-mark"></span>
      <span class="brand-name">quolbi</span>
    </div>
  </section>

  <section class="card card-back">
    <svg class="sweep" viewBox="0 0 520 300" width="520" height="300" aria-hidden="true">
      <path d="M0 202 C210 202 430 170 500 0 L520 0 L520 300 L0 300 Z" fill="var(--band-grey)"/>
      <path d="M0 214 C215 214 445 182 520 22 L520 300 L0 300 Z" fill="var(--card-white)"/>
      <path d="M0 220 C215 220 447 190 520 34 L520 300 L0 300 Z" fill="var(--teal)"/>
    </svg>

    <div class="person">
      <p class="person-name">Marla Whitcombe</p>
      <p class="person-title">Owner</p>
    </div>

    <div class="brand">
      <span class="brand-mark"></span>
      <span class="brand-name">quolbi</span>
    </div>

    <div class="phones">
      <p>P: 512 555 0148</p>
      <p>F: 512 555 0162</p>
    </div>

    <div class="contact">
      <p>marla@quolbi.com</p>
      <p>www.quolbi.com</p>
      <p>2817 Maple Hollow Ln Austin TX 78529</p>
    </div>
  </section>
</body>
</html>
```